Onlineshop für hochwertige Gebrauchtsättel für den Reitsport sucht Webdesign
Zielgruppe
Wir verkaufen hochwertige Gebrauchtsättel für den Reitsport und möchten Reiter jeder Altersgruppe ansprechen.
Aufgabenstellung
Farbgebung : grün braun (eventuell gelb), naturnahe Farben
Ein Logo ist bereits vorhanden.

```html
<!DOCTYPE html>
<html lang="de">
<head>
<meta charset="utf-8">
<title>Oakridge Saddlery – Über uns</title>
<link href="https://fonts.googleapis.com/css2?family=Montserrat:wght@400;500;600;700&display=swap" rel="stylesheet">
<style>
  :root {
    --green: #7aa82e;
    --brown: #6b4a1f;
    --text: #3c3c3c;
    --rule: #8a8a8a;
    --footer: #4a4a4a;
    --white: #ffffff;
    --black: #000000;
  }
  * { margin: 0; padding: 0; box-sizing: border-box; }
  html, body { width: 999px; height: 1200px; overflow: hidden; background: var(--white); }
  body { font-family: "Montserrat", sans-serif; color: var(--text); position: relative; }

  .site-header { height: 64px; display: flex; align-items: center; justify-content: center; }
  .brand-name { font-size: 30px; font-weight: 500; color: var(--brown); letter-spacing: 1px; }

  .main-nav { position: absolute; top: 64px; left: 0; width: 999px; height: 33px; background: var(--green);
    display: flex; justify-content: flex-end; align-items: center; padding-right: 109px; box-shadow: 0 1px 2px rgba(0,0,0,.2); }
  .main-nav a { color: var(--white); text-decoration: none; font-size: 13px; padding: 0 20px; line-height: 23px;
    border-left: 1px solid var(--white); }
  .main-nav a:first-child { border-left: none; padding-left: 0; font-weight: 600; }
  .main-nav a:last-child { padding-right: 0; }

  .hero { position: absolute; top: 121px; left: 109px; width: 781px; height: 286px; background: var(--black); overflow: hidden; }
  .hero-photo { position: absolute; right: 110px; top: 0; width: 280px; height: 286px;
    background: radial-gradient(ellipse at 60% 40%, #6a3a1c 0%, #3a1f0e 40%, #000 75%); }
  .hero-title { position: absolute; left: 26px; top: 27px; width: 380px; color: var(--white);
    font-size: 22px; font-weight: 600; line-height: 30px; }
  .hero-link { position: absolute; left: 26px; bottom: 20px; color: var(--white); text-decoration: none; font-size: 12.5px; font-weight: 500; }

  .usp-band { position: absolute; top: 431px; left: 109px; width: 781px; height: 39px; background: var(--green);
    color: var(--white); font-size: 15px; font-weight: 500; display: flex; align-items: center; justify-content: center; }

  .team { position: absolute; top: 506px; left: 0; width: 999px; }
  .member { position: absolute; width: 185px; text-align: center; }
  .member:nth-child(1) { left: 149px; }
  .member:nth-child(2) { left: 407px; }
  .member:nth-child(3) { left: 665px; }
  .member-photo { width: 185px; height: 185px; border-radius: 50%; }
  .photo-a { background: radial-gradient(circle at 40% 40%, #c9c2b8 0%, #7d5a34 50%, #3b2a1a 100%); }
  .photo-b { background: radial-gradient(circle at 50% 55%, #5a6b4a 0%, #8a7e74 55%, #b9b1aa 100%); }
  .photo-c { background: radial-gradient(circle at 50% 45%, #e0b9a0 0%, #b88a5a 45%, #3f4a2c 100%); }
  .member-card { margin-top: 13px; border-top: 1px solid var(--rule); border-bottom: 1px solid var(--rule); height: 77px; padding-top: 12px; }
  .member-name { color: var(--green); font-size: 15px; font-weight: 500; }
  .member-role { font-size: 14px; margin-top: 7px; }

  .intro { position: absolute; top: 809px; left: 109px; width: 781px; text-align: center; }
  .intro-lead { font-size: 12.6px; font-weight: 700; line-height: 17.3px; }
  .intro-body { font-size: 12.4px; line-height: 17.3px; margin-top: 17px; }

  .site-footer { position: absolute; top: 1149px; left: 0; width: 999px; height: 51px; background: var(--footer);
    border-top: 1px solid #777; color: var(--white); font-size: 11px; }
  .copyright { position: absolute; left: 109px; top: 23px; }
  .footer-nav { position: absolute; right: 109px; top: 15px; display: flex; }
  .footer-nav a { color: var(--white); text-decoration: none; padding: 0 13px; line-height: 24px; border-left: 1px solid var(--white); }
  .footer-nav a:first-child { border-left: none; }
  .footer-nav a:last-child { padding-right: 0; }
  .footer-badge { position: absolute; left: 451px; top: 1089px; width: 97px; height: 97px; border-radius: 50%;
    background: var(--white); border: 2px solid #ddd; display: flex; align-items: center; justify-content: center;
    font-size: 10px; font-weight: 600; color: var(--brown); text-align: center; line-height: 13px; }
</style>
</head>
<body>
  <header class="site-header">
    <div class="brand-name">OAKRIDGE SADDLERY</div>
  </header>

  <nav class="main-nav">
    <a href="#">Über Oakridge Saddlery</a>
    <a href="#">Gebrauchtsättel</a>
    <a href="#">Qualitätsversprechen</a>
    <a href="#">Preisliste</a>
    <a href="#">Dirketanfrage</a>
    <a href="#">Kontakt</a>
  </nav>

  <section class="hero">
    <div class="hero-photo" role="img" aria-label="Foto: braunes Pferd mit Trense vor schwarzem Hintergrund"></div>
    <h1 class="hero-title">Seit über 12 Jahren versorgen wir unsere Kunden mit gebrauchten Sätteln in geprüfter Qualität.</h1>
    <a class="hero-link" href="#">Über Oakridge Saddlery &nbsp;&gt;</a>
  </section>

  <div class="usp-band">Qualitätskontrolle durch Oakridge Saddlery · Kostenlose Lieferung · Auf Anfrage 30 Tage Probezeit</div>

  <section class="team">
    <div class="member">
      <div class="member-photo photo-a" role="img" aria-label="Foto: Geschäftsführerin mit Schimmel im Herbstlicht"></div>
      <div class="member-card"><div class="member-name">Lena Brandt</div><div class="member-role">Geschäftsführerin</div></div>
    </div>
    <div class="member">
      <div class="member-photo photo-b" role="img" aria-label="Foto: Sattlermeister im grünen Pullover auf einer Straße"></div>
      <div class="member-card"><div class="member-name">Jonas Keller</div><div class="member-role">Sattlermeister</div></div>
    </div>
    <div class="member">
      <div class="member-photo photo-c" role="img" aria-label="Foto: Sattlermeisterin im Gegenlicht im Grünen"></div>
      <div class="member-card"><div class="member-name">Carla Wendt</div><div class="member-role">Sattlermeisterin</div></div>
    </div>
  </section>

  <section class="intro">
    <p class="intro-lead">Sitae aut litium ipiet, cus is sundias eum facimentiam fuga. Nam inihil in et est et occum voluptae ent ium ad quatust, nobit qui dellautem sincia comniminci dolorenimus, que laborrorro quo quatibusciae natium as abore offic te nosaectae evelibus. De dolor ate plaborumqui volorecti ut eum harcilit odistio vendi serro eosaniasped eum rem iduciis suntemo luptatem volores soluptaquas a samusam rerum fugaccuptatur.</p>
    <p class="intro-body">Qui aliaepe nimus eum hillaut emquossimpor arum repererum cusam fugit facidelest essi cuptatur, tem. Nam, unto vero iur aut faccum et as rest, natasitatios quam simusa exceratem labo. Modicips ameturi tem lam et fuga. Ut liciam, tem nus etus, omnisima verum eum lab iligendam, con presciet et, sa nusdand endisqui odisquo dipsae estem acestem. Tem. Pe consequae pla consequas aturit aut autessenet eossuntus, se odit aut aut omnimin imusae nam vellorum et as conse prepe aut licimolut volorum aspic tescimpore remolore, quibusa pitatus mos num fugiam re, cust, sumet qui omni omnim qui autenemodi re perepudantis as doluptae non pore quunt. Laboribus sunt ut volupid quam qui quam, quas atempe dia quam aut volorum fugitatem consendic tem nitias dem. Sa pelest libusdaeria ipiet re reperum ipsa int volumque site nimus inis eos rerios quae nobis prempor ibearum apis abo. Et dolorecaes atia nobis quo estem dis et omnis et perferum sum alibear ibustem qui quam intempor aci.</p>
  </section>

  <footer class="site-footer">
    <div class="copyright">© Copyright by Oakridge Saddlery GmbH</div>
    <nav class="footer-nav">
      <a href="#">Kontakt</a>
      <a href="#">Datenschutz</a>
      <a href="#">Impressum</a>
    </nav>
  </footer>
  <div class="footer-badge">Oakridge<br>Saddlery</div>
</body>
</html>
```